Create a business promotion flyer to leave in customer mailboxes. We are a bulk petroleum supplier, servicing any industry that requires diesel. Base in griffith NSW, servicing griffith area and surrounds.

Business Name - Terra Petro
Fuel@terrapetro-example.com.au
Marco - 0400 000 001 mtorrisi@terrapetro-example.com.au
Liam - 0400 000 002 lharcourt@terrapetro-example.com.au
Peter - 0400 000 003 pwinslow@terrapetro-example.com.au
Office 02 5550 0100

Bulk Fuel deliveries.
Oils & lubricants
Local Family owned business

```html
<!DOCTYPE html>
<html lang="en">
<head>
<meta charset="utf-8">
<title>Terra Petro – Bulk Fuel Flyer</title>
<link href="https://fonts.googleapis.com/css2?family=Barlow:wght@700;800&family=Poppins:wght@400;500;600&display=swap" rel="stylesheet">
<style>
  :root {
    --red: #ed1c24;
    --ink: #231f20;
    --charcoal: #252325;
    --sand: #e0dbd4;
    --white: #ffffff;
    --backdrop: #5a5b5d;
  }
  * { margin: 0; padding: 0; box-sizing: border-box; }
  html, body { width: 1051px; height: 1200px; overflow: hidden; }
  body { background: var(--backdrop); font-family: "Poppins", sans-serif; }

  .flyer {
    position: absolute; left: 77px; top: 20px;
    width: 897px; height: 1160px;
    background: var(--sand); overflow: hidden;
  }
  .hero-photo {
    position: absolute; left: 0; top: 0; width: 897px; height: 440px;
    background: linear-gradient(180deg, #9fb4d6 0%, #dfe6f1 35%, #b9bcc2 62%, #8a8d92 78%, var(--sand) 100%);
  }
  .brand {
    position: absolute; left: 72px; top: 78px;
    display: flex; align-items: center; gap: 12px;
  }
  .brand-dot { width: 22px; height: 22px; border-radius: 50%; background: var(--red); }
  .brand-name { font-size: 42px; font-weight: 500; color: var(--red); letter-spacing: -0.5px; }

  .tagline-box {
    position: absolute; left: 652px; top: 0; width: 212px; height: 256px;
    background: var(--red); color: var(--white);
    display: flex; align-items: center; justify-content: center; text-align: center;
    font-size: 21.5px; line-height: 28px; padding-top: 8px;
  }
  .tagline-box strong { font-weight: 600; }

  .headline {
    position: absolute; left: 72px; top: 406px;
    font-family: "Barlow", sans-serif; font-weight: 800;
    font-size: 62px; line-height: 66px; color: var(--ink); letter-spacing: -0.5px;
  }
  .headline .accent { color: var(--red); }

  .timeline { position: absolute; left: 0; top: 0; }

  .feature { position: absolute; top: 672px; color: var(--ink); }
  .feature h2 { font-size: 27px; line-height: 32px; font-weight: 600; letter-spacing: -0.3px; }
  .feature p { margin-top: 8px; font-size: 16px; line-height: 21px; }
  .feature-bulk { left: 79px; }
  .feature-oils { left: 334px; top: 674px; }
  .feature-local { left: 601px; top: 674px; }

  .contact-band {
    position: absolute; left: 0; top: 844px; width: 897px; height: 240px;
    background: var(--charcoal); color: var(--white);
  }
  .cta { position: absolute; left: 76px; top: 34px; }
  .cta h3 { font-size: 35px; line-height: 45px; font-weight: 500; }
  .cta p { margin-top: 6px; font-size: 18px; font-weight: 500; }

  .contact { position: absolute; }
  .contact-row { display: flex; align-items: center; gap: 8px; }
  .contact-row svg { flex: none; width: 10px; height: 12px; }
  .contact-name { font-size: 21px; font-weight: 500; line-height: 26px; }
  .contact-phone { font-size: 22px; font-weight: 600; line-height: 28px; }
  .contact-email { font-size: 12.5px; line-height: 22px; }
  .c-marco { left: 342px; top: 34px; }
  .c-peter { left: 342px; top: 144px; }
  .c-liam { left: 627px; top: 37px; }
  .c-office { left: 627px; top: 156px; }

  .email-bar {
    position: absolute; left: 0; top: 1084px; width: 897px; height: 76px;
    background: var(--red); color: var(--white);
    display: flex; align-items: center; justify-content: center; gap: 14px;
  }
  .email-bar .ask { font-size: 16.5px; }
  .mail-badge {
    width: 34px; height: 34px; border-radius: 50%; background: var(--charcoal);
    display: flex; align-items: center; justify-content: center;
  }
  .email-bar .address { font-size: 22px; font-weight: 600; }
</style>
</head>
<body>
<main class="flyer">
  <div class="hero-photo" role="img" aria-label="Photo of a white road train with two fuel tankers parked in front of a large steel depot shed under a blue cloudy sky"></div>

  <div class="brand">
    <span class="brand-dot"></span>
    <span class="brand-name">Terra Petro</span>
  </div>

  <div class="tagline-box">
    <p>Reliable bulk<br>fuel supply<br>across <strong>Griffith</strong><br>and surrounds</p>
  </div>

  <h1 class="headline"><span class="accent">FUEL FOR</span> FARMING,<br>TRANSPORT &amp; INDUSTRY</h1>

  <svg class="timeline" width="897" height="700" viewBox="0 0 897 700" aria-hidden="true">
    <line x1="123" y1="613" x2="720" y2="613" stroke="#ed1c24" stroke-width="1"/>
    <circle cx="720" cy="613" r="2" fill="#ed1c24"/>
    <circle cx="123" cy="613" r="39" fill="#ed1c24"/>
    <circle cx="382" cy="613" r="39" fill="#ed1c24"/>
    <circle cx="645" cy="613" r="39" fill="#ed1c24"/>
    <!-- fuel pump -->
    <g fill="none" stroke="#fff" stroke-width="1.8" stroke-linejoin="round">
      <rect x="108" y="594" width="22" height="36" rx="2"/>
      <rect x="112" y="598" width="14" height="8"/>
      <path d="M119 612c-3 4-4 6-4 8a4 4 0 0 0 8 0c0-2-1-4-4-8z"/>
      <path d="M104 632h30"/>
      <path d="M130 604l6 5v16a2 2 0 0 0 4 0v-14l-3-4"/>
    </g>
    <!-- oil can -->
    <g fill="none" stroke="#fff" stroke-width="1.8" stroke-linejoin="round">
      <path d="M368 602h26v30h-30v-26z"/>
      <path d="M366 600l-4-4 4-4 4 4"/>
      <path d="M364 624h30"/>
      <path d="M376 610c-2 3-3 5-3 6a3 3 0 0 0 6 0c0-1-1-3-3-6z"/>
      <rect x="383" y="609" width="5" height="9" rx="2.5"/>
    </g>
    <!-- group -->
    <g fill="none" stroke="#fff" stroke-width="1.8">
      <circle cx="632" cy="604" r="5"/>
      <circle cx="645" cy="606" r="5"/>
      <circle cx="658" cy="604" r="5"/>
      <path d="M623 622v-3a9 9 0 0 1 13-8"/>
      <path d="M636 628v-5a9 9 0 0 1 18 0v5"/>
      <path d="M667 622v-3a9 9 0 0 0-13-8"/>
    </g>
  </svg>

  <section class="feature feature-bulk">
    <h2>Bulk Fuel<br>deliveries.</h2>
    <p>Reliable diesel supply<br>for any industry.</p>
  </section>
  <section class="feature feature-oils">
    <h2>Oils &amp;<br>lubricants</h2>
    <p>Quality products to keep<br>your equipment<br>performing at its best.</p>
  </section>
  <section class="feature feature-local">
    <h2>Local Family<br>owned business</h2>
    <p>Proudly supporting our<br>local community.</p>
  </section>

  <section class="contact-band">
    <div class="cta">
      <h3>Need fuel<br>for your<br>operation?</h3>
      <p>Contact Us</p>
    </div>

    <div class="contact c-marco">
      <div class="contact-row"><svg viewBox="0 0 10 12"><circle cx="5" cy="3" r="3" fill="#ed1c24"/><path d="M0 12a5 5 0 0 1 10 0z" fill="#ed1c24"/></svg><span class="contact-name">Marco</span></div>
      <div class="contact-row"><svg viewBox="0 0 10 12"><path d="M2 1l2 0 1 3-1.5 1a6 6 0 0 0 2.5 4l1-1.5 2.5 1.5v2l-1 1C4 11 0 6 1 2z" fill="#ed1c24"/></svg><span class="contact-phone">0400 000 001</span></div>
      <div class="contact-row"><svg viewBox="0 0 10 12"><rect x="0" y="3" width="10" height="7" fill="#ed1c24"/><path d="M0 3l5 4 5-4" stroke="#252325" fill="none"/></svg><span class="contact-email">mtorrisi@terrapetro-example.com.au</span></div>
    </div>

    <div class="contact c-peter">
      <div class="contact-row"><svg viewBox="0 0 10 12"><circle cx="5" cy="3" r="3" fill="#ed1c24"/><path d="M0 12a5 5 0 0 1 10 0z" fill="#ed1c24"/></svg><span class="contact-name">Peter</span></div>
      <div class="contact-row"><svg viewBox="0 0 10 12"><path d="M2 1l2 0 1 3-1.5 1a6 6 0 0 0 2.5 4l1-1.5 2.5 1.5v2l-1 1C4 11 0 6 1 2z" fill="#ed1c24"/></svg><span class="contact-phone">0400 000 003</span></div>
      <div class="contact-row"><svg viewBox="0 0 10 12"><rect x="0" y="3" width="10" height="7" fill="#ed1c24"/><path d="M0 3l5 4 5-4" stroke="#252325" fill="none"/></svg><span class="contact-email">pwinslow@terrapetro-example.com.au</span></div>
    </div>

    <div class="contact c-liam">
      <div class="contact-row"><svg viewBox="0 0 10 12"><circle cx="5" cy="3" r="3" fill="#ed1c24"/><path d="M0 12a5 5 0 0 1 10 0z" fill="#ed1c24"/></svg><span class="contact-name">Liam</span></div>
      <div class="contact-row"><svg viewBox="0 0 10 12"><path d="M2 1l2 0 1 3-1.5 1a6 6 0 0 0 2.5 4l1-1.5 2.5 1.5v2l-1 1C4 11 0 6 1 2z" fill="#ed1c24"/></svg><span class="contact-phone">0400 000 002</span></div>
      <div class="contact-row"><svg viewBox="0 0 10 12"><rect x="0" y="3" width="10" height="7" fill="#ed1c24"/><path d="M0 3l5 4 5-4" stroke="#252325" fill="none"/></svg><span class="contact-email">lharcourt@terrapetro-example.com.au</span></div>
    </div>

    <div class="contact c-office">
      <div class="contact-row"><svg viewBox="0 0 10 12"><rect x="0" y="4" width="4" height="8" fill="none" stroke="#ed1c24"/><rect x="4" y="1" width="6" height="11" fill="none" stroke="#ed1c24"/></svg><span class="contact-name">Office</span></div>
      <div class="contact-row"><svg viewBox="0 0 10 12"><path d="M2 1l2 0 1 3-1.5 1a6 6 0 0 0 2.5 4l1-1.5 2.5 1.5v2l-1 1C4 11 0 6 1 2z" fill="#ed1c24"/></svg><span class="contact-phone">02 5550 0100</span></div>
    </div>
  </section>

  <footer class="email-bar">
    <span class="ask">Have questions? Email us at:</span>
    <span class="mail-badge"><svg width="16" height="12" viewBox="0 0 16 12" aria-hidden="true"><rect x="0.5" y="0.5" width="15" height="11" fill="#fff"/><path d="M0.5 0.5l7.5 6 7.5-6" stroke="#252325" fill="none"/></svg></span>
    <span class="address">Fuel@terrapetro-example.com.au</span>
  </footer>
</main>
</body>
</html>
```